We have a parent company, Summit Harbor Group (SHG), that has other company partners. We are looking for ways to incorporate our SHG logo with our network partners, Beacon Ledger and The Blue Gate. My initial thought is to have SHG as front of card logo, and include The Blue Gate and Beacon Ledger logos on back but I'm open to ideas. Card should include website www.summitharborgrp.example (use for reference). Keywords "Tax Services" "Real Estate" "Insurance" "Investments" "Chief Financial Officer"

Industry/Entity Type

Financial

```html
<!DOCTYPE html>
<html lang="en">
<head>
<meta charset="utf-8">
<title>Summit Harbor Group – Business Card</title>
<link rel="stylesheet" href="https://fonts.googleapis.com/css2?family=Inter:wght@400;600;700&display=swap">
<style>
  :root {
    --backdrop: #c9cacb;
    --card-white: #e7e7e9;
    --brand-blue: #0b4a96;
    --brand-red: #c8202a;
    --text-grey: #4a4d52;
    --strip-white: #e9e9eb;
    --divider: #b9bbbf;
  }
  * { box-sizing: border-box; margin: 0; padding: 0; }
  html, body {
    width: 1200px; height: 1038px; overflow: hidden;
    background: var(--backdrop);
    font-family: "Inter", Arial, sans-serif;
  }
  .card {
    position: absolute; left: 300px; width: 602px; height: 333px;
    overflow: hidden;
  }
  .card-front { top: 138px; background: var(--card-white); }
  .card-back { top: 542px; background: var(--brand-blue); }

  .brand-name {
    display: flex; align-items: center; gap: 10px;
    font-weight: 700; font-size: 22px; letter-spacing: 0.5px;
    white-space: nowrap;
  }
  .brand-dot { width: 16px; height: 16px; border-radius: 50%; background: var(--brand-red); flex: none; }
  .card-front .brand-name { position: absolute; left: 178px; top: 152px; transform: translateX(-50%); color: var(--brand-blue); }

  .front-divider { position: absolute; left: 326px; top: 92px; width: 1px; height: 148px; background: var(--divider); }

  .contact { position: absolute; left: 356px; top: 88px; color: var(--text-grey); }
  .contact-name { color: var(--brand-blue); font-weight: 700; font-size: 19px; line-height: 1.2; }
  .contact-title { font-size: 13px; margin-bottom: 14px; }
  .contact-list { list-style: none; font-size: 13.5px; line-height: 18.5px; }
  .contact-list li { display: flex; align-items: center; gap: 8px; }
  .contact-list svg { width: 14px; height: 14px; flex: none; }
  .contact-address { font-size: 13.5px; line-height: 17px; margin-top: 14px; }

  .card-back .brand-name { position: absolute; left: 301px; top: 118px; transform: translateX(-50%); color: #ffffff; font-size: 28px; }
  .partner-strip {
    position: absolute; left: 0; top: 206px; width: 100%; height: 59px;
    background: var(--strip-white);
  }
  .partner-name {
    position: absolute; top: 50%; transform: translate(-50%, -50%);
    font-weight: 700; font-size: 20px; white-space: nowrap;
  }
  .partner-gate { left: 112px; color: var(--brand-blue); }
  .partner-ledger { left: 452px; color: var(--brand-red); }
  .services {
    position: absolute; left: 0; top: 285px; width: 100%;
    text-align: center; color: #ffffff; font-size: 15px;
  }
</style>
</head>
<body>
  <section class="card card-front">
    <div class="brand-name"><span class="brand-dot"></span>Summit Harbor Group</div>
    <div class="front-divider"></div>
    <div class="contact">
      <p class="contact-name">Daniel Ashcombe</p>
      <p class="contact-title">Founder &amp; CEO</p>
      <ul class="contact-list">
        <li>
          <svg viewBox="0 0 14 14"><path d="M3 1.5l2 .3.8 3-1.3 1a7 7 0 0 0 3.7 3.7l1-1.3 3 .8.3 2c-.2.8-1 1.5-1.8 1.5C5.6 12.5 1.5 8.4 1.5 3.3 1.5 2.5 2.2 1.7 3 1.5z" fill="var(--brand-blue)"/></svg>
          555-014-2736
        </li>
        <li>
          <svg viewBox="0 0 14 14"><rect x="1" y="3" width="12" height="8.5" fill="var(--brand-blue)"/><path d="M1.5 3.5L7 8l5.5-4.5" stroke="var(--card-white)" stroke-width="1.2" fill="none"/></svg>
          info@summitharborgrp.example
        </li>
        <li>
          <svg viewBox="0 0 14 14" fill="none" stroke="var(--brand-blue)" stroke-width="1.1"><circle cx="7" cy="7" r="5.8"/><ellipse cx="7" cy="7" rx="2.5" ry="5.8"/><path d="M1.2 7h11.6M2 4h10M2 10h10"/></svg>
          www.summitharborgrp.example
        </li>
      </ul>
      <p class="contact-address">2200 Ridgeview Lane<br>Cedar Falls, CO 80000</p>
    </div>
  </section>

  <section class="card card-back">
    <div class="brand-name"><span class="brand-dot"></span>Summit Harbor Group</div>
    <div class="partner-strip">
      <span class="partner-name partner-gate">The Blue Gate</span>
      <span class="partner-name partner-ledger">Beacon Ledger</span>
    </div>
    <p class="services">Tax Services · Real Estate · Insurance · Investments · Chief Financial Officer</p>
  </section>
</body>
</html>
```